Lumora Learning Web Design Project

Who We are:
Lumora Learning is education information portal/ magazine, providing information about the Chinese and International education markets. Our aim is to help school principals improve there curriculum, and parents in understanding this curriculum.

Project Brief:
The site will include education news updates, educational services, curriculum developments and overseas study. We hope the site represents the cross cultural bridge between the west and east. The site will cover both the Sciences and Arts.

Note:
The logo design competition is also underway so we only need the website design

What We want:
This competition is for Design only no coding!
Design a home page based on Template 1,2 or 3. I only need to select one.
The design of an article page.

Optional
Design a Microsoft Windows metro style splash page.

Sites We like:
http://www.kavelin.com.cn/kavelinlingo/default.aspx
http://www.brixtalacademia.co.uk/
http://qrpv.norvatestudio.net/

Template Explanations:
Template 1-
The main information has a dynamic sliding category view that when clicked displays the relevant info.
In addition to the main upper menu it also has a left hand sliding menu that pops out on click or gesture

Template 2-
Has limited number of Articles most of the menus are drop downs from the top menu

Template 3-
No Top menu

Target Market(s)

Teachers, principals and parents

Industry/Entity Type

Education

Requirements
Should not have
• kindergarten preschool feel

```html
<!DOCTYPE html>
<html lang="en">
<head>
<meta charset="utf-8">
<title>Lumora Learning</title>
<link href="https://fonts.googleapis.com/css2?family=Roboto+Condensed:wght@400;700&family=Arimo:wght@400;700&display=swap" rel="stylesheet">
<style>
:root{
  --page:#d9d9d9;
  --white:#ffffff;
  --red:#e5241b;
  --nav-dark:#353535;
  --nav-mid:#4a4a4a;
  --ink:#111111;
  --body-text:#6b6b6b;
  --muted:#9a9a9a;
  --rule:#e3e3e3;
  --link-blue:#1a6fc4;
  --panel-head:#ececec;
  --search-btn:#2a6aa8;
  --green:#7aa32a;
  --fb-blue:#3b8fd0;
}
*{box-sizing:border-box;margin:0;padding:0}
html,body{width:885px;height:1200px;overflow:hidden;background:var(--page)}
body{font-family:"Arimo",Arial,sans-serif;color:var(--ink)}
.page{position:relative;width:885px;height:1200px;overflow:hidden;background:var(--page)}

/* header */
.site-header{position:absolute;left:0;top:0;width:885px;height:96px;background:var(--white)}
.brand{position:absolute;left:98px;top:30px;display:flex;align-items:center;gap:8px}
.brand-dot{width:26px;height:26px;border-radius:50%;background:var(--red)}
.brand-name{font-family:"Roboto Condensed",sans-serif;font-weight:700;font-size:18px;color:var(--red);letter-spacing:.3px}
.search{position:absolute;left:545px;top:30px;width:236px;height:34px;border-radius:4px;background:#e6e6e6;border:1px solid #d2d2d2;padding:3px}
.search-field{position:absolute;left:4px;top:4px;width:168px;height:24px;background:linear-gradient(#f3f3f3,#e4e4e4);border:1px solid #d6d6d6;font-size:9px;color:#777;padding:7px 0 0 7px}
.search-btn{position:absolute;left:169px;top:3px;width:61px;height:26px;background:linear-gradient(#3a7cc0,#1f5a95);border-radius:2px;color:#fff;font-family:"Roboto Condensed",sans-serif;font-weight:700;font-size:12px;text-align:center;line-height:26px}

/* nav */
.main-nav{position:absolute;left:0;top:96px;width:885px;height:34px;background:linear-gradient(var(--nav-mid),var(--nav-dark));border-bottom:4px solid var(--red)}
.main-nav ul{list-style:none;position:absolute;left:104px;top:0;height:30px;display:flex}
.main-nav li{font-family:"Roboto Condensed",sans-serif;font-weight:700;font-size:13px;color:#fff;height:30px;line-height:31px;padding:0 9px 0 7px;margin-right:10px}
.main-nav li.active{background:var(--red);padding:0 8px 0 7px}

/* hero */
.hero{position:absolute;left:103px;top:145px;width:679px;height:298px;background:var(--white);padding:7px;box-shadow:0 1px 2px rgba(0,0,0,.15)}
.hero-photo{width:665px;height:284px;background:linear-gradient(90deg,#c9ccd0 0%,#eef0f2 35%,#d7dce4 55%,#c8b9b0 80%,#dfe2e6 100%)}
.hero-arrow{position:absolute;top:140px;width:14px;height:14px}
.hero-arrow.prev{left:6px}
.hero-arrow.next{right:6px}

/* boxes */
.box{position:absolute;background:var(--white);box-shadow:0 1px 2px rgba(0,0,0,.15)}
.side-title{display:flex;align-items:center;gap:8px;padding:10px 7px 0 7px;font-family:"Roboto Condensed",sans-serif;font-weight:700;font-size:12px;color:#222;height:30px;border-bottom:1px solid var(--rule);margin:0 0 4px 0}
.side-title .line{flex:1;height:2px;background:var(--red)}
.side-title .line.green{background:var(--green)}
.side-title .line.blue{background:var(--fb-blue)}

.cat-list{list-style:none;padding:2px 0 0 8px}
.cat-list li{font-size:9px;height:19.4px;line-height:19.4px;display:flex;align-items:center;gap:6px;color:#222}
.cat-list li::before{content:"";width:0;height:0;border-left:3px solid var(--red);border-top:2.5px solid transparent;border-bottom:2.5px solid transparent}

.social{display:flex;gap:8px;padding:12px 0 0 16px}
.social span{width:24px;height:24px;border-radius:3px}
.social .s-chirp{background:#5ab4e6}
.social .s-friend{background:#3b5998}
.social .s-link{background:#1b86bd}
.social .s-view{background:#d8261c}

.fb-widget{position:absolute;left:8px;top:42px;width:139px;height:201px;border:1px solid #c8c8c8;padding:7px}
.fb-top{display:flex;gap:6px;padding-bottom:8px;border-bottom:1px solid #e6e6e6}
.fb-mark{width:30px;height:30px;background:#e9edf4;border-radius:50%}
.fb-name{font-size:9px;font-weight:700;color:#3b5998}
.fb-like{margin-top:3px;width:34px;height:13px;border:1px solid #cfcfcf;background:#f2f2f2;font-size:8px;color:#333;line-height:11px;text-align:center}
.fb-count{font-size:7.5px;color:#333;padding:6px 0 5px}
.fb-count b{font-weight:400;color:#3b5998}
.fb-faces{display:grid;grid-template-columns:repeat(3,34px);gap:3px}
.fb-faces span{height:34px}
.fb-foot{margin-top:6px;border-top:1px solid #e6e6e6;padding-top:5px;font-size:7px;color:#555;display:flex;align-items:center;gap:4px}
.fb-foot i{width:8px;height:8px;background:#3b5998;display:block}

/* tabs & articles */
.tabs{position:absolute;left:0;top:0;width:353px;height:34px;border-bottom:1px solid var(--rule);display:flex}
.tab{font-family:"Roboto Condensed",sans-serif;font-weight:700;font-size:12px;height:34px;line-height:34px;padding:0 12px;color:#aaa;border-right:1px solid var(--rule)}
.tab.active{background:var(--red);color:#fff;position:relative}
.tab.active::after{content:"";position:absolute;left:29px;bottom:-5px;border-top:5px solid var(--red);border-left:5px solid transparent;border-right:5px solid transparent}

.article{position:absolute;left:14px;width:325px;height:116px;border-bottom:1px solid var(--rule)}
.thumb{position:absolute;left:0;top:0;width:87px;height:87px;background:#e6e6e6;padding:4px}
.thumb span{display:block;width:79px;height:79px}
.article h3{position:absolute;left:97px;top:0;font-size:10.5px;line-height:14px;font-weight:700;color:#111;white-space:nowrap}
.article p{position:absolute;left:96px;top:31px;font-size:8.6px;line-height:14px;color:var(--body-text);white-space:nowrap}
.article .more{position:absolute;left:97px;top:93px;font-size:7.5px;color:var(--link-blue)}

/* right panels */
.panel-head{height:33px;background:var(--panel-head);font-family:"Roboto Condensed",sans-serif;font-weight:700;font-size:12px;color:#666;padding:9px 0 0 10px}
.news-list{list-style:none;padding:7px 7px 0 7px}
.news-list li{height:51.3px;border-bottom:1px solid var(--rule);padding-top:3px}
.news-list li:last-child{border-bottom:0}
.news-date{font-size:7.5px;color:var(--muted);margin-bottom:3px}
.news-text{font-size:8.6px;line-height:12.5px;color:#111;white-space:nowrap}
.news-text a{color:var(--red);text-decoration:none}

/* footer */
.footer-nav{position:absolute;left:104px;top:1141px;width:684px;height:26px;background:linear-gradient(#fbfbfb,#e6e6e6);box-shadow:0 1px 1px rgba(0,0,0,.12)}
.footer-nav ul{list-style:none;display:flex;position:absolute;left:166px;top:0}
.footer-nav li{font-size:8.5px;color:#444;line-height:26px;margin-right:0}
.copyright{position:absolute;left:0;top:1180px;width:885px;text-align:center;font-size:8.5px;color:#555}
</style>
</head>
<body>
<div class="page">

  <header class="site-header">
    <div class="brand"><span class="brand-dot"></span><span class="brand-name">LUMORA LEARNING</span></div>
    <div class="search">
      <div class="search-field">Search</div>
      <div class="search-btn">SEARCH</div>
    </div>
  </header>

  <nav class="main-nav">
    <ul>
      <li class="active">HOME</li>
      <li>ABOUT US</li>
      <li>CATEGORIES</li>
      <li>ARTICLES</li>
      <li>BLOG</li>
      <li>CONTACT US</li>
    </ul>
  </nav>

  <section class="hero">
    <div class="hero-photo" role="img" aria-label="Teacher and smiling students in a science classroom in front of a periodic table"></div>
    <svg class="hero-arrow prev" viewBox="0 0 14 14"><path d="M9 2 L4 7 L9 12" fill="none" stroke="#111" stroke-width="2.4"/></svg>
    <svg class="hero-arrow next" viewBox="0 0 14 14"><path d="M5 2 L10 7 L5 12" fill="none" stroke="#111" stroke-width="2.4"/></svg>
  </section>

  <!-- left column -->
  <aside class="box" style="left:104px;top:449px;width:155px;height:311px">
    <div class="side-title">CATEGORIES <span class="line"></span></div>
    <ul class="cat-list">
      <li>Lorem ipsum dolor</li><li>Lorem ipsum dolor</li><li>Lorem ipsum dolor</li><li>Lorem ipsum dolor</li>
      <li>Lorem ipsum dolor</li><li>Lorem ipsum dolor</li><li>Lorem ipsum dolor</li><li>Lorem ipsum dolor</li>
      <li>Lorem ipsum dolor</li><li>Lorem ipsum dolor</li><li>Lorem ipsum dolor</li><li>Lorem ipsum dolor</li>
      <li>Lorem ipsum dolor</li><li>Lorem ipsum dolor</li>
    </ul>
  </aside>

  <aside class="box" style="left:104px;top:767px;width:155px;height:80px">
    <div class="side-title">FOLLOW US <span class="line green"></span></div>
    <div class="social">
      <span class="s-chirp" aria-label="Chirpline"></span>
      <span class="s-friend" aria-label="Friendbook"></span>
      <span class="s-link" aria-label="Linkvale"></span>
      <span class="s-view" aria-label="ViewTube"></span>
    </div>
  </aside>

  <aside class="box" style="left:104px;top:854px;width:155px;height:252px">
    <div class="side-title">FRIENDBOOK <span class="line blue"></span></div>
    <div class="fb-widget">
      <div class="fb-top">
        <span class="fb-mark"></span>
        <div><div class="fb-name">Lumora Learning</div><div class="fb-like">Like</div></div>
      </div>
      <div class="fb-count">13,223 people like <b>Lumora Learning</b>.</div>
      <div class="fb-faces">
        <span role="img" aria-label="Member photo" style="background:#6f7f98"></span>
        <span role="img" aria-label="Member photo" style="background:#a8745a"></span>
        <span role="img" aria-label="Member photo" style="background:#b08a7a"></span>
        <span role="img" aria-label="Member photo" style="background:#3f4f6a"></span>
        <span role="img" aria-label="Member photo" style="background:#9a7a66"></span>
        <span role="img" aria-label="Member photo" style="background:#6a5aa0"></span>
        <span role="img" aria-label="Member photo" style="background:#5a7088"></span>
        <span role="img" aria-label="Member photo" style="background:#8a8278"></span>
        <span role="img" aria-label="Member photo" style="background:#c9d0de"></span>
      </div>
      <div class="fb-foot"><i></i>Friendbook social plugin</div>
    </div>
  </aside>

  <!-- main column -->
  <main class="box" style="left:266px;top:449px;width:353px;height:678px">
    <div class="tabs"><div class="tab active">SCIENCES</div><div class="tab">ARTS</div></div>

    <article class="article" style="top:48px">
      <div class="thumb"><span role="img" aria-label="Student in safety goggles doing a lab experiment" style="background:linear-gradient(135deg,#c7d6e6,#4a74b0)"></span></div>
      <h3>Lorem ipsum dolor sit amet, consectetur<br>adipisicing elit, sed do eiusmod.</h3>
      <p>Sed ut perspiciatis unde omnis iste natus error sit<br>voluptatem accusantium doloremque laudantium, totam<br>rem aperiam, eaque ipsa quae ab illo inventore veritatis et<br>quasi architecto beatae vitae dicta sunt explicabo.</p>
      <div class="more">Full Article +</div>
    </article>

    <article class="article" style="top:177px">
      <div class="thumb"><span role="img" aria-label="Colourful icons rising from an open book" style="background:radial-gradient(circle at 50% 40%,#6a3a7a,#111 70%)"></span></div>
      <h3>Lorem ipsum dolor sit amet, consectetur<br>adipisicing elit, sed do eiusmod tempor.</h3>
      <p>Sed ut perspiciatis unde omnis iste natus error sit<br>voluptatem accusantium doloremque laudantium, totam<br>rem aperiam, eaque ipsa quae ab illo inventore veritatis et<br>quasi architecto beatae vitae dicta sunt explicabo.</p>
      <div class="more">Full Article +</div>
    </article>

    <article class="article" style="top:306px">
      <div class="thumb"><span role="img" aria-label="Dictionary entry for education under a pen" style="background:linear-gradient(135deg,#e8e2d6,#bfb29a)"></span></div>
      <h3>Lorem ipsum dolor sit amet, consectetur<br>adipisicing elit, sed do eiusmod.</h3>
      <p>Sed ut perspiciatis unde omnis iste natus error sit<br>voluptatem accusantium doloremque laudantium, totam<br>rem aperiam, eaque ipsa quae ab illo inventore veritatis et<br>quasi architecto beatae vitae dicta sunt explicabo.</p>
      <div class="more">Full Article +</div>
    </article>

    <article class="article" style="top:435px">
      <div class="thumb"><span role="img" aria-label="E-reader standing among hardback books" style="background:linear-gradient(135deg,#3a3a3a,#111 60%,#c9c2b0)"></span></div>
      <h3>Lorem ipsum dolor sit amet, consectetur<br>adipisicing elit, sed do eiusmod tempor.</h3>
      <p>Sed ut perspiciatis unde omnis iste natus error sit<br>voluptatem accusantium doloremque laudantium, totam<br>rem aperiam, eaque ipsa quae ab illo inventore veritatis et<br>quasi architecto beatae vitae dicta sunt explicabo.</p>
      <div class="more">Full Article +</div>
    </article>

    <article class="article" style="top:564px;border-bottom:0">
      <div class="thumb"><span role="img" aria-label="E-reader standing among hardback books" style="background:linear-gradient(135deg,#3a3a3a,#111 60%,#c9c2b0)"></span></div>
      <h3>Lorem ipsum dolor sit amet, consectetur<br>adipisicing elit, sed do eiusmod tempor.</h3>
      <p>Sed ut perspiciatis unde omnis iste natus error sit<br>voluptatem accusantium doloremque laudantium, totam<br>rem aperiam, eaque ipsa quae ab illo inventore veritatis et<br>quasi architecto beatae vitae dicta sunt explicabo.</p>
      <div class="more">Full Article +</div>
    </article>
  </main>

  <!-- right column -->
  <aside class="box" style="left:626px;top:449px;width:155px;height:290px">
    <div class="panel-head">EDUCATION NEWS UPDATES</div>
    <ul class="news-list">
      <li><div class="news-date">19-07-2013</div><div class="news-text">Lorem ipsum dolor sit amet, cons<br>ectetur adipisicing elit. <a>Read more...</a></div></li>
      <li><div class="news-date">16-07-2013</div><div class="news-text">Lorem ipsum dolor sit amet, cons<br>ectetur adipisicing elit. <a>Read more...</a></div></li>
      <li><div class="news-date">12-07-2013</div><div class="news-text">Lorem ipsum dolor sit amet, cons<br>ectetur adipisicing elit. <a>Read more...</a></div></li>
      <li><div class="news-date">11-07-2013</div><div class="news-text">Lorem ipsum dolor sit amet, cons<br>ectetur adipisicing elit. <a>Read more...</a></div></li>
      <li><div class="news-date">10-07-2013</div><div class="news-text">Lorem ipsum dolor sit amet, cons<br>ectetur adipisicing elit. <a>Read more...</a></div></li>
    </ul>
  </aside>

  <aside class="box" style="left:626px;top:746px;width:155px;height:290px">
    <div class="panel-head">ARTICLES</div>
    <ul class="news-list">
      <li><div class="news-date">19-07-2013</div><div class="news-text">Lorem ipsum dolor sit amet, cons<br>ectetur adipisicing elit. <a>Read more...</a></div></li>
      <li><div class="news-date">19-07-2013</div><div class="news-text">Lorem ipsum dolor sit amet, cons<br>ectetur adipisicing elit. <a>Read more...</a></div></li>
      <li><div class="news-date">19-07-2013</div><div class="news-text">Lorem ipsum dolor sit amet, cons<br>ectetur adipisicing elit. <a>Read more...</a></div></li>
      <li><div class="news-date">19-07-2013</div><div class="news-text">Lorem ipsum dolor sit amet, cons<br>ectetur adipisicing elit. <a>Read more...</a></div></li>
      <li><div class="news-date">19-07-2013</div><div class="news-text">Lorem ipsum dolor sit amet, cons<br>ectetur adipisicing elit. <a>Read more...</a></div></li>
    </ul>
  </aside>

  <footer>
    <nav class="footer-nav">
      <ul>
        <li style="margin-right:42px">Home</li>
        <li style="margin-right:30px">About Us</li>
        <li style="margin-right:30px">Categories</li>
        <li style="margin-right:30px">Articles</li>
        <li style="margin-right:30px">BLog</li>
        <li>Contact Us</li>
      </ul>
    </nav>
    <div class="copyright">Copyright ©&nbsp; 2013 Lumora Learning. All rights reserved.</div>
  </footer>

</div>
</body>
</html>
```